mailer to distressed properties

Our business is a company that buys houses for cash that are in need of repairs. Need to create a post card to mail to homeowners to get them to call us to give them a price on their home for cash and purchase it. Would like a run down house on background and our company info so they could call us. Have a logo would like to incorporate in it. Want to get to the point across we can buy there home for cash on any condition and close quickly. We can also buy them if they have permit or violation issues. We also buy homes going into foreclosure so we can stop foreclosure. Company name is R & T Dwellings. P o box 829 Fernwick my 10472. 555-214-8693. Email us at info@rntdwellings.example and our website Rntdwellings.example. Open to a lot of direct designs excited to see what you come up with. Anything else you can think we are open to see it. Email us with any other questions . Also can add fast closing and save no real estate commissions collected. We want it in color your choice. Also on font open to anything and size of font.

Target Market(s)

Run down and distressed properties

Industry/Entity Type

Construction Company

Font styles to use
Serif
Sans Serif

Requirements
Must have
• A background of a distressed home and our info how to call us
Nice to have
• Colorful and attractive
Should not have
• Nothing I can think of

```html
<!DOCTYPE html>
<html lang="en">
<head>
<meta charset="utf-8">
<title>R &amp; T Dwellings – Cash Offer Postcard</title>
<link rel="stylesheet" href="https://fonts.googleapis.com/css2?family=Fira+Sans:wght@400;500;700;800&family=Fira+Sans+Condensed:wght@400;500;600;700&family=Montserrat:wght@500;600;800;900&display=swap">
<style>
  :root {
    --red: #e3161e;
    --red-dark: #b50f15;
    --yellow: #ffd21f;
    --orange: #f7a11a;
    --ink: #1a1a1a;
    --panel: rgba(20, 20, 22, 0.82);
    --paper: #ffffff;
    --mist: #f1f1f1;
    --rule: #cfcfcf;
    --backdrop: #e8e5e0;
    --text-font: "Fira Sans", Arial, sans-serif;
    --cond-font: "Fira Sans Condensed", "Arial Narrow", sans-serif;
    --display-font: "Montserrat", Arial, sans-serif;
  }
  * { box-sizing: border-box; margin: 0; padding: 0; }
  html, body { width: 1073px; height: 1200px; overflow: hidden; }
  body { background: var(--backdrop); font-family: var(--text-font); position: relative; }

  .postcard { position: absolute; width: 743px; height: 481px; background: var(--paper); overflow: hidden; }

  /* ---------- Front ---------- */
  .front { left: 93px; top: 73px; }
  .front .top-band { position: absolute; left: 0; top: 0; width: 100%; height: 20px; background: linear-gradient(var(--red), var(--red-dark)); z-index: 3; }
  .front .house-photo { position: absolute; left: 0; top: 20px; width: 420px; height: 461px;
    background: linear-gradient(180deg, #23469c 0%, #3f66b3 35%, #c9b79a 60%, #8a7a5e 82%, #5d6b3c 100%); }
  .front .cash-photo { position: absolute; left: 400px; top: 20px; width: 343px; height: 461px;
    background: linear-gradient(160deg, #1f4aa8 0%, #d8dad6 35%, #a9aca6 60%, #cfa58a 85%, #1f4aa8 100%); }
  .front .panel { position: absolute; left: 34px; top: 20px; width: 277px; height: 451px; background: var(--panel); z-index: 2; }
  .front .brand { position: absolute; top: 19px; width: 100%; text-align: center; font-family: var(--text-font); font-weight: 400; font-size: 34px; line-height: 40px; color: #e9e9e9; letter-spacing: 0.5px; }
  .front .lead { position: absolute; left: 42px; top: 86px; font-family: var(--display-font); font-weight: 600; font-size: 16px; line-height: 15px; color: #fff; letter-spacing: 0.8px; }
  .front .cash { position: absolute; left: 40px; top: 118px; font-family: var(--display-font); font-weight: 900; font-size: 64px; line-height: 1; letter-spacing: -1px;
    background: linear-gradient(180deg, #fff27a 0%, var(--yellow) 45%, var(--orange) 100%); -webkit-background-clip: text; background-clip: text; color: transparent; }
  .front .bang { position: absolute; left: 236px; top: 76px; font-family: var(--display-font); font-weight: 900; font-size: 104px; line-height: 1;
    background: linear-gradient(180deg, #fff27a, var(--yellow) 50%, var(--orange)); -webkit-background-clip: text; background-clip: text; color: transparent; }
  .front .promise { position: absolute; top: 212px; width: 100%; text-align: center; font-family: var(--cond-font); font-weight: 500; font-size: 22px; line-height: 28px; color: #fff; }
  .front .checklist { position: absolute; left: 30px; top: 248px; list-style: none; width: 300px; }
  .front .checklist li { display: flex; align-items: center; gap: 12px; height: 26px; font-family: var(--cond-font); font-weight: 500; font-size: 17px; color: #fff; text-transform: uppercase; white-space: nowrap; }
  .front .checklist svg { flex: none; }
  .front .phone-band { position: absolute; left: 28px; top: 376px; width: 287px; height: 45px; background: linear-gradient(var(--red), var(--red-dark)); z-index: 3;
    display: flex; align-items: center; justify-content: center; gap: 10px; font-family: var(--cond-font); font-weight: 600; font-size: 26px; color: #fff; }
  .front .phone-band svg { flex: none; }
  .front .site { position: absolute; top: 424px; left: 34px; width: 277px; text-align: center; z-index: 3; font-family: var(--text-font); font-weight: 500; font-size: 13px; line-height: 18px; letter-spacing: 1.2px; color: #fff; }
  .front .tagline-band { position: absolute; left: 392px; top: 425px; width: 351px; height: 56px; border-radius: 10px 0 0 0; z-index: 3;
    background: linear-gradient(180deg, var(--yellow), var(--orange)); display: flex; align-items: center; justify-content: center;
    font-family: var(--cond-font); font-weight: 500; font-size: 15px; color: var(--red); }

  /* ---------- Back ---------- */
  .back { left: 193px; top: 619px; }
  .back .curve-art { position: absolute; left: 0; top: 0; }
  .back .brand-block { position: absolute; left: 0; top: 44px; width: 440px; display: flex; align-items: center; justify-content: center; gap: 12px; }
  .back .brand-square { width: 34px; height: 34px; background: var(--ink); }
  .back .brand-name { font-family: var(--text-font); font-weight: 800; font-size: 36px; color: var(--ink); }
  .back .headline-banner { position: absolute; left: 0; top: 146px; width: 476px; height: 103px; background: linear-gradient(var(--red), #c4121a); box-shadow: 0 2px 3px rgba(0,0,0,0.25);
    text-align: center; font-family: var(--cond-font); font-weight: 700; }
  .back .headline-banner .line-one { display: block; margin-top: 14px; font-size: 32px; line-height: 36px; color: #fff; }
  .back .headline-banner .line-two { display: block; font-size: 32px; line-height: 40px; color: var(--yellow); margin-left: -22px; }
  .back .pitch { position: absolute; left: 29px; top: 260px; width: 405px; font-family: var(--cond-font); font-size: 14.5px; line-height: 17px; color: var(--ink); }
  .back .contact-band { position: absolute; left: 0; top: 338px; width: 400px; height: 80px; }
  .back .contact-band .band-shape { position: absolute; left: 0; top: 0; }
  .back .contact-phone { position: absolute; left: 70px; top: 8px; display: flex; align-items: center; gap: 12px; font-family: var(--cond-font); font-weight: 700; font-size: 35px; line-height: 40px; color: var(--red); white-space: nowrap; }
  .back .contact-phone svg { flex: none; }
  .back .contact-site { position: absolute; left: 72px; top: 50px; font-family: var(--text-font); font-weight: 500; font-size: 21px; line-height: 26px; letter-spacing: 2px; color: var(--ink); white-space: nowrap; }
  .back .return-address { position: absolute; left: 474px; top: 31px; font-family: var(--cond-font); font-style: normal; font-size: 11px; line-height: 13px; color: var(--ink); }
  .back .return-address .sender { font-size: 14px; line-height: 16px; }
  .back .stamp-box { position: absolute; left: 637px; top: 28px; width: 89px; height: 56px; border: 1px solid var(--rule); }
  .back .address-lines { position: absolute; left: 505px; top: 143px; width: 220px; }
  .back .address-lines span { display: block; height: 31px; border-bottom: 1px solid var(--rule); }
</style>
</head>
<body>

<section class="postcard front" aria-label="Postcard front">
  <div class="top-band"></div>
  <div class="house-photo" role="img" aria-label="Photo of a two-storey house with blue sky"></div>
  <div class="cash-photo" role="img" aria-label="Photo of a hand holding a fan of hundred-dollar bills"></div>

  <div class="panel">
    <div class="brand">R&amp;T dwellings</div>
    <div class="lead">QUICKLY SELL YOUR<br>HOUSE FAST FOR</div>
    <div class="cash">CA$H</div>
    <div class="bang">!</div>
    <div class="promise">We'll Buy Your Home</div>
    <ul class="checklist">
      <li><svg width="16" height="16" viewBox="0 0 16 16"><circle cx="8" cy="8" r="8" fill="#ffd21f"/><path d="M4.5 8.2l2.3 2.2 4.7-4.8" fill="none" stroke="#8a5a00" stroke-width="1.6"/></svg>With cash</li>
      <li><svg width="16" height="16" viewBox="0 0 16 16"><circle cx="8" cy="8" r="8" fill="#ffd21f"/><path d="M4.5 8.2l2.3 2.2 4.7-4.8" fill="none" stroke="#8a5a00" stroke-width="1.6"/></svg>In any condition</li>
      <li><svg width="16" height="16" viewBox="0 0 16 16"><circle cx="8" cy="8" r="8" fill="#ffd21f"/><path d="M4.5 8.2l2.3 2.2 4.7-4.8" fill="none" stroke="#8a5a00" stroke-width="1.6"/></svg>Foreclosure</li>
      <li><svg width="16" height="16" viewBox="0 0 16 16"><circle cx="8" cy="8" r="8" fill="#ffd21f"/><path d="M4.5 8.2l2.3 2.2 4.7-4.8" fill="none" stroke="#8a5a00" stroke-width="1.6"/></svg>Permit or violation issues</li>
    </ul>
  </div>

  <div class="phone-band">
    <svg width="22" height="22" viewBox="0 0 22 22"><rect width="22" height="22" rx="4" fill="#f7a11a"/><path d="M7 4.5c.6 0 1 .3 1.2.8l.9 2.2c.2.5 0 1-.4 1.3l-1 .8c.7 1.5 1.9 2.7 3.4 3.4l.8-1c.3-.4.8-.6 1.3-.4l2.2.9c.5.2.8.6.8 1.2v1.6c0 .8-.7 1.4-1.5 1.3C9.6 16.2 5.8 12.4 5.4 6c0-.8.5-1.5 1.3-1.5z" fill="#e3161e"/></svg>
    555-214-8693
  </div>
  <div class="site">www.rntdwellings.example</div>
  <div class="tagline-band">ANY CONDITION, ANI SITUATION, ANY PROBLEM</div>
</section>

<section class="postcard back" aria-label="Postcard back">
  <svg class="curve-art" width="743" height="481" viewBox="0 0 743 481">
    <path d="M0 0 H380 C440 40 470 100 476 160 C470 260 440 350 340 420 H0 Z" fill="#f1f1f1"/>
    <path d="M380 0 C430 30 462 90 476 160 L456 160 C448 100 420 40 370 0 Z" fill="#c4121a"/>
    <path d="M476 250 C468 320 440 380 400 418 L392 418 C430 378 454 320 458 250 Z" fill="#c4121a"/>
  </svg>

  <div class="brand-block">
    <span class="brand-square"></span>
    <span class="brand-name">R &amp; T Dwellings</span>
  </div>

  <div class="headline-banner">
    <span class="line-one">QUICKLY SELL YOUR HOUSE</span>
    <span class="line-two">FAST FOR CASH</span>
  </div>

  <p class="pitch">We'll give you top dollar for your house, accept it in any condition, and take you through the whole process quickly. Our team is local and made up of licensed and insured home builders and real estate professionals who have a proven track record.</p>

  <div class="contact-band">
    <svg class="band-shape" width="400" height="80" viewBox="0 0 400 80">
      <defs>
        <linearGradient id="bandFill" x1="0" x2="1" y1="0" y2="0">
          <stop offset="0" stop-color="#ffd21f"/>
          <stop offset="1" stop-color="#f7a11a"/>
        </linearGradient>
      </defs>
      <path d="M0 0 H400 L336 80 H0 Z" fill="url(#bandFill)"/>
    </svg>
    <div class="contact-phone">
      <svg width="30" height="30" viewBox="0 0 22 22"><rect width="22" height="22" rx="4" fill="#e3161e"/><path d="M7 4.5c.6 0 1 .3 1.2.8l.9 2.2c.2.5 0 1-.4 1.3l-1 .8c.7 1.5 1.9 2.7 3.4 3.4l.8-1c.3-.4.8-.6 1.3-.4l2.2.9c.5.2.8.6.8 1.2v1.6c0 .8-.7 1.4-1.5 1.3C9.6 16.2 5.8 12.4 5.4 6c0-.8.5-1.5 1.3-1.5z" fill="#f7a11a"/></svg>
      <span>555-214-8693</span>
    </div>
    <div class="contact-site">www.rntdwellings.example</div>
  </div>

  <address class="return-address">
    <div class="sender">R &amp; T Dwellings.</div>
    P.O. Box 829<br>
    Fernwick NY 10472<br>
    555-214-8693<br>
    info@rntdwellings.example
  </address>
  <div class="stamp-box"></div>
  <div class="address-lines"><span></span><span></span><span></span><span></span><span></span></div>
</section>

</body>
</html>
```